Healer at the Hearth needs business card

We need a business card that reflects the look and feel of the new website at www.healerathehearth.ca

Our patient navigation and advocacy services are most commonly used by seniors who feel overwhelmed by the health care system and want someone on their side to advocate for their care. Individuals with ill parents or other family members may also come to rely on Healer at the Hearth to help them support their loved one through their health care journey. Ultimately, anyone who finds their health care experience challenging and wants someone completely focused on their needs can benefit from the services of our doctor / nurse team.

Business

Must have
• One design tailored for two clinician which should include: logo, name, title, tel, email, web address and tagline
Nice to have
• A banner image to create a similar look to the website at www.healerathehearth.ca
Should not have
• Too cluttered or busy - must be clean and professional

```html
<!DOCTYPE html>
<html lang="en">
<head>
<meta charset="utf-8">
<title>Healer at the Hearth — Business Card</title>
<link rel="stylesheet" href="https://fonts.googleapis.com/css2?family=Open+Sans:wght@400;600&family=Questrial&display=swap">
<style>
  :root {
    --canvas: #ecebe8;
    --card: #ffffff;
    --band: #efefef;
    --ink: #3a3a3a;
    --ink-soft: #555555;
    --accent-red: #c8343c;
    --photo-light: #eaf1f6;
    --photo-mid: #c9dbe6;
    --photo-teal: #2fa79a;
    --photo-skin: #e7bfa4;
  }
  * { box-sizing: border-box; margin: 0; padding: 0; }
  html, body {
    width: 1200px; height: 1000px; overflow: hidden;
    background: var(--canvas);
    font-family: "Open Sans", Verdana, sans-serif;
    color: var(--ink);
  }
  .sheet {
    position: relative; width: 1200px; height: 1000px;
    display: flex; flex-direction: column; align-items: center; justify-content: center;
    gap: 64px;
  }
  .card {
    position: relative; width: 660px; height: 378px;
    background: var(--card);
    box-shadow: 0 6px 24px rgba(0,0,0,.14);
    overflow: hidden;
  }

  /* Front */
  .card-front__banner {
    position: absolute; inset: 0 0 auto 0; height: 212px;
    background:
      radial-gradient(ellipse 40% 55% at 62% 62%, var(--photo-skin) 0%, rgba(231,191,164,.6) 45%, rgba(231,191,164,0) 75%),
      radial-gradient(ellipse 22% 30% at 38% 8%, var(--photo-teal) 0%, rgba(47,167,154,0) 80%),
      linear-gradient(100deg, var(--photo-light) 0%, var(--photo-mid) 45%, var(--photo-light) 100%);
  }
  .card-front__identity {
    position: absolute; left: 0; right: 0; top: 98px; text-align: center;
    padding-left: 150px;
  }
  .card-front__name {
    font-family: "Questrial", "Century Gothic", sans-serif;
    font-size: 34px; font-weight: 400; color: #fff; letter-spacing: .5px;
    text-shadow: 1px 2px 3px rgba(0,0,0,.45);
  }
  .card-front__title {
    font-size: 14px; font-weight: 600; color: #fff; margin-top: 2px;
    text-shadow: 1px 1px 2px rgba(0,0,0,.45);
  }
  .card-front__tagline {
    position: absolute; left: 0; right: 0; top: 240px; text-align: center;
    font-size: 17px; letter-spacing: .5px; color: var(--ink);
  }
  .card-front__contacts {
    position: absolute; left: 34px; right: 34px; top: 290px; height: 56px;
    background: var(--band);
    display: flex; align-items: center; justify-content: space-between;
    padding: 0 22px; font-size: 13px; color: var(--ink-soft);
  }
  .contact { display: flex; align-items: center; gap: 6px; white-space: nowrap; }
  .contact__icon { width: 15px; height: 15px; flex: none; }
  .contact__at { color: var(--accent-red); font-size: 15px; font-weight: 600; }

  /* Back */
  .card-back__decor {
    position: absolute; inset: 0;
    background:
      radial-gradient(ellipse 18% 14% at 62% 40%, rgba(231,191,164,.18) 0%, rgba(231,191,164,0) 100%),
      linear-gradient(120deg, #f6f6f6 0%, #ffffff 50%, #f4f4f4 100%);
  }
  .card-back__brand {
    position: absolute; inset: 0;
    display: flex; align-items: center; justify-content: center;
  }
  .brand__name {
    font-family: "Open Sans", Verdana, sans-serif;
    font-size: 30px; font-weight: 400; letter-spacing: .5px;
    color: var(--ink);
    white-space: nowrap;
  }
</style>
</head>
<body>
<main class="sheet">

  <section class="card card-front" aria-label="Business card front">
    <div class="card-front__banner" role="img" aria-label="Banner photo of a caregiver's hands holding a patient's hand"></div>
    <div class="card-front__identity">
      <p class="card-front__name">Person Name</p>
      <p class="card-front__title">Tiltle</p>
    </div>
    <p class="card-front__tagline">" TagLine TagLine TagLine "</p>
    <div class="card-front__contacts">
      <span class="contact contact--phone">
        <svg class="contact__icon" viewBox="0 0 24 24" aria-hidden="true">
          <path fill="#c8343c" d="M6.6 10.8a15.1 15.1 0 0 0 6.6 6.6l2.2-2.2a1 1 0 0 1 1-.25 11.4 11.4 0 0 0 3.6.57 1 1 0 0 1 1 1V20a1 1 0 0 1-1 1A17 17 0 0 1 3 4a1 1 0 0 1 1-1h3.5a1 1 0 0 1 1 1c0 1.25.2 2.45.57 3.57a1 1 0 0 1-.25 1z"/>
        </svg>: 1234567890
      </span>
      <span class="contact contact--email">
        <span class="contact__at">@</span>: xxxxxxx@xxxxxxxxxx.xxx
      </span>
      <span class="contact contact--web">
        <svg class="contact__icon" viewBox="0 0 24 24" aria-hidden="true">
          <path fill="#c8343c" d="M5 2h10l5 5v15H5z"/>
          <path fill="#fff" d="M8 11h9v1.5H8zm0 3.5h9V16H8zm0 3.5h6v1.5H8z"/>
        </svg>: www.healerathehearth.ca
      </span>
    </div>
  </section>

  <section class="card card-back" aria-label="Business card back">
    <div class="card-back__decor" role="img" aria-label="Faint background photo of a stethoscope"></div>
    <div class="card-back__brand">
      <p class="brand__name">Healer at the Hearth</p>
    </div>
  </section>

</main>
</body>
</html>
```